Flyer-Design für Einzel- und Großhandel für Tuningteile
Zielgruppe
Die HLV GmbH ist im Einzel- und Großhandel für Tuningteile seit 9 Jahren tätig. Schwerpunktmäßig beschäftigen wir uns mit AERO Carbon Anbauteilen aus Carbon, Ansaugsystemen, Tuningboxen, Ladeluftkühlern, Bremsen und Kupplungen. Wir betrieben 7 Onlineshops die nach Themen oder Ländern gegliedert sind.
Gesucht wird ein Paketbeileger, der ausschließlich in unsere eigenen Pakete beigelegt wird. Zielgruppe sind also Bestandskunden - Alter, Einkommen ist stark gemischt. Unsere Zielgruppe ist zu 95+% männlich.
Aufgabenstellung
Der Paketbeileger soll 3 Zwecke erfüllen:
1. Ein persönliches Danke für deine Bestellung von der Geschäftsführung/dem Team von HLV.
2. Eine Bitte, uns auf Sicher Kaufen, Plauderbuch oder Findolo zu bewerten (Versionen mit 5% Incentive und ohne)
3. Ein Hinweis darauf, dass wir 5 unterschiedliche Onlineshops haben:
- www.hl-vortex.de : Hochwertige Carbon Autoteile und Norvalo Ansaugsysteme
- www.tq7-laden.de: TQ7 von Winkel Rennwerk. Die besten Tuningboxen aus den USA!
- www.pmlkuehl.de: Hochleistungs Ladeluftkühler zu günstigen Preisen.
- www.stark-kiste.de: Hochfeste Pellham Motorsport-Kupplungen.
- www.haltekeil.de: Die besten Bremsen zu besten Preisen.
- www.dröhnrohr.de: Die besten Sportauspuffanlagen. Gönn dir laut!
(Das Wording kann gerne anders sein!)
Ansprüche an das Design:
- Der Flyer muss sehr hochwertig wirken und wird später auf entsprechendem Material gedruckt.
- Der Look muss exklusiv und qualitativ hochwertig sein.
- Maße sind frei wählbar. Das Design steht hier im Vordergrund. Alles was gut und exklusiv aussieht geht.
- Optimal wäre es, wenn die 3 Geschäftsführer mit Bild und eventuell Zitat im Flyer zu sehen sind.
Die Ziele des Flyers sind:
1. Zum WOW-Effekt beim Auspacken beizutragen
2. Bewertungen zu generieren
3. Cross-Sales in den anderen Shops anzustoßen und den Kunden klarmachen, welche Bandbreite von Produkten bei uns erhältlich ist.

```html
<!DOCTYPE html>
<html lang="de">
<head>
<meta charset="utf-8">
<title>HL Vortex – Paketbeileger</title>
<link href="https://fonts.googleapis.com/css2?family=Raleway:wght@400;500;600;700;800&display=swap" rel="stylesheet">
<style>
  :root{
    --backdrop:#a4a8b6;
    --photo-top:#8a8a8a;
    --photo-mid:#3c3c3c;
    --photo-bottom:#161616;
    --paper:#efeeea;
    --inside-top:#d6d6d4;
    --inside-bottom:#b4b4b2;
    --ink:#262626;
    --ink-soft:#4a4a4a;
    --rule:#8c8c8c;
    --portrait:#7a7a7a;
    --white:#ffffff;
  }
  *{box-sizing:border-box;}
  html,body{margin:0;padding:0;width:1200px;height:1091px;overflow:hidden;}
  body{background:var(--backdrop);font-family:"Raleway",sans-serif;position:relative;}

  .flyer{position:absolute;left:60px;top:275px;width:1080px;height:540px;display:flex;box-shadow:0 14px 40px rgba(0,0,0,.22);}
  .panel{position:relative;width:540px;height:540px;overflow:hidden;}

  /* Cover */
  .cover{background:var(--paper);}
  .cover-photo{position:absolute;inset:0;width:540px;height:540px;}
  .brand{position:absolute;left:150px;bottom:76px;display:flex;align-items:center;gap:12px;color:var(--white);}
  .brand-mark{width:20px;height:20px;background:var(--white);}
  .brand-name{font-weight:800;font-size:19px;letter-spacing:.08em;text-transform:uppercase;}

  /* Inside */
  .inside{background:linear-gradient(180deg,var(--inside-top),var(--inside-bottom));color:var(--ink);padding:34px 40px 0;}
  .inside-title{margin:0;font-weight:700;font-size:34px;letter-spacing:.02em;text-transform:uppercase;line-height:1.1;}
  .inside-sub{margin:4px 0 0;font-weight:400;font-size:16px;color:var(--ink-soft);}

  .shop-list{list-style:none;margin:20px 0 0;padding:0;display:grid;grid-template-columns:1fr 1fr;column-gap:24px;row-gap:12px;}
  .shop-url{display:block;font-weight:700;font-size:13px;}
  .shop-text{display:block;font-weight:400;font-size:12px;line-height:1.35;color:var(--ink-soft);}

  .thanks{margin-top:18px;padding-top:14px;border-top:1px solid var(--rule);display:flex;gap:16px;align-items:center;}
  .team{display:flex;gap:8px;}
  .team-portrait{width:52px;height:52px;background:var(--portrait);}
  .thanks-title{margin:0;font-weight:700;font-size:17px;}
  .thanks-text{margin:3px 0 0;font-size:12px;line-height:1.35;color:var(--ink-soft);}

  .review{margin:12px 0 0;font-size:12px;line-height:1.4;}
  .review strong{font-weight:700;}

  .inside-footer{position:absolute;left:0;right:0;bottom:16px;margin:0;text-align:center;font-weight:600;font-size:12px;letter-spacing:.08em;text-transform:uppercase;color:var(--ink);}
</style>
</head>
<body>
  <div class="flyer">
    <section class="panel cover">
      <svg class="cover-photo" viewBox="0 0 540 540" role="img" aria-label="Schwarzweißfoto: schwarzes Sportcoupé von hinten bei Nacht vor Bäumen und Stadtkulisse, das Heck ragt in den hellen Randstreifen">
        <defs>
          <linearGradient id="coverTone" x1="0" y1="0" x2="0" y2="1">
            <stop offset="0" stop-color="#8a8a8a"/>
            <stop offset=".45" stop-color="#3c3c3c"/>
            <stop offset="1" stop-color="#161616"/>
          </linearGradient>
        </defs>
        <path d="M0 0H440V150H500V370H440V540H0Z" fill="url(#coverTone)"/>
      </svg>
      <div class="brand">
        <span class="brand-mark"></span>
        <span class="brand-name">HL Vortex</span>
      </div>
    </section>

    <section class="panel inside">
      <h2 class="inside-title">Unsere Onlineshops</h2>
      <p class="inside-sub">Von Ansaugsystemen bis zu echten carbon teilen</p>

      <ul class="shop-list">
        <li><span class="shop-url">www.hl-vortex.de</span><span class="shop-text">Hochwertige Carbon Autoteile und Norvalo Ansaugsysteme</span></li>
        <li><span class="shop-url">www.tq7-laden.de</span><span class="shop-text">TQ7 von Winkel Rennwerk. Die besten Tuningboxen aus den USA!</span></li>
        <li><span class="shop-url">www.pmlkuehl.de</span><span class="shop-text">Hochleistungs Ladeluftkühler zu günstigen Preisen</span></li>
        <li><span class="shop-url">www.stark-kiste.de</span><span class="shop-text">Hochfeste Pellham Motorsport-Kupplungen</span></li>
        <li><span class="shop-url">www.haltekeil.de</span><span class="shop-text">Die besten Bremsen zu besten Preisen</span></li>
        <li><span class="shop-url">www.dröhnrohr.de</span><span class="shop-text">Die besten Sportauspuffanlagen. Gönn dir laut!</span></li>
      </ul>

      <div class="thanks">
        <div class="team">
          <div class="team-portrait" role="img" aria-label="Porträtfoto Geschäftsführer 1"></div>
          <div class="team-portrait" role="img" aria-label="Porträtfoto Geschäftsführer 2"></div>
          <div class="team-portrait" role="img" aria-label="Porträtfoto Geschäftsführer 3"></div>
        </div>
        <div>
          <p class="thanks-title">Danke für deine Bestellung!</p>
          <p class="thanks-text">Deine Geschäftsführung und das ganze Team der HLV GmbH</p>
        </div>
      </div>

      <p class="review">Zufrieden? Bewerte uns auf <strong>Sicher Kaufen</strong>, <strong>Plauderbuch</strong> oder <strong>Findolo</strong> und sichere dir 5 % auf deine nächste Bestellung.</p>

      <p class="inside-footer">Gönn dir neue Möglichkeiten!</p>
    </section>
  </div>
</body>
</html>
```